Cards and Stationary for natural and holistic Earthing/Grounding products
Solvana Portugal
Cards and Stationary for natural and holistic Earthing/Grounding products - Health
Creative Brief
Bright & Fun-filled
Miro T. Kastelan, PhD
Solvana Portugal Founder
Rua dos Pinheiros Altos 14 2615-117, Vale Serrado, Portugal
info@solvanaportugal.pt
www.solvanaportugal.pt
The back of the card should incorporate the logo and web address.

```html
<!DOCTYPE html>
<html lang="en">
<head>
<meta charset="utf-8">
<title>Solvana Portugal – Business Card</title>
<link rel="stylesheet" href="https://fonts.googleapis.com/css2?family=Montserrat:wght@400;500;600;700&display=swap">
<style>
  :root {
    --bg: #d9d9d9;
    --card: #ffffff;
    --ink: #2b2b2b;
    --muted: #5a5a5a;
    --green: #3f9b35;
    --green-light: #8cc63f;
    --green-dark: #2e7d2a;
  }
  * { margin: 0; padding: 0; box-sizing: border-box; }
  html, body {
    width: 1200px; height: 799px; overflow: hidden;
    background: var(--bg);
    font-family: "Montserrat", Arial, sans-serif;
  }
  .stage {
    position: relative; width: 1200px; height: 799px;
    display: flex; align-items: center; justify-content: center; gap: 40px;
  }
  .card {
    position: relative; width: 540px; height: 309px;
    background: var(--card);
    box-shadow: 0 10px 24px rgba(0,0,0,0.18);
  }
  /* Front */
  .card-front .accent-bar {
    position: absolute; left: 0; top: 150px; width: 7px; height: 60px;
    background: var(--green);
  }
  .identity { position: absolute; left: 34px; top: 150px; }
  .identity .name {
    font-weight: 700; font-size: 19px; color: var(--ink); letter-spacing: 0.2px;
  }
  .identity .role {
    margin-top: 4px; font-size: 13px; font-weight: 500; color: var(--green);
    padding-bottom: 6px; border-bottom: 1.5px solid var(--green-light);
    display: inline-block;
  }
  .address {
    position: absolute; left: 34px; top: 220px;
    display: flex; gap: 10px; align-items: flex-start;
    font-size: 11px; line-height: 16px; color: var(--muted);
  }
  .brand-mark {
    position: absolute; right: 42px; top: 34px;
    display: flex; align-items: center; gap: 10px;
  }
  .brand-dot { width: 34px; height: 34px; border-radius: 50%; background: var(--green-light); }
  .brand-name {
    font-weight: 600; font-size: 22px; color: var(--green); line-height: 1.1;
  }
  .contacts {
    position: absolute; left: 318px; top: 150px; list-style: none;
    font-size: 10.5px; color: var(--muted);
  }
  .contacts li { display: flex; align-items: center; gap: 10px; height: 18px; }
  .contacts svg { flex: none; }
  /* Back */
  .card-back {
    display: flex; flex-direction: column; align-items: center; justify-content: center;
  }
  .back-brand { display: flex; align-items: center; gap: 16px; }
  .back-brand .brand-dot { width: 62px; height: 62px; }
  .back-brand .brand-name { font-size: 38px; }
  .web {
    margin-top: 34px; font-size: 14px; font-weight: 600; color: var(--green-dark);
    letter-spacing: 0.4px;
  }
</style>
</head>
<body>
<main class="stage">
  <section class="card card-front" aria-label="Business card front">
    <div class="brand-mark">
      <span class="brand-dot"></span>
      <span class="brand-name">Solvana Portugal</span>
    </div>

    <span class="accent-bar"></span>
    <div class="identity">
      <p class="name">Miro T. Kastelan, PhD</p>
      <p class="role">Solvana Portugal Founder</p>
    </div>

    <div class="address">
      <svg width="12" height="16" viewBox="0 0 12 16" aria-hidden="true">
        <path d="M6 0a6 6 0 0 0-6 6c0 4.5 6 10 6 10s6-5.5 6-10a6 6 0 0 0-6-6z" fill="var(--green)"/>
        <circle cx="6" cy="6" r="2.2" fill="#fff"/>
      </svg>
      <p>Rua dos Pinheiros Altos 14<br>2615-117, Vale Serrado, Portugal</p>
    </div>

    <ul class="contacts">
      <li>
        <svg width="10" height="14" viewBox="0 0 10 14" aria-hidden="true">
          <rect x="0.5" y="0.5" width="9" height="13" rx="1.5" fill="none" stroke="var(--ink)"/>
          <circle cx="5" cy="11" r="0.9" fill="var(--ink)"/>
        </svg>
        +351 912 408 336
      </li>
      <li>
        <svg width="12" height="9" viewBox="0 0 12 9" aria-hidden="true">
          <rect x="0.5" y="0.5" width="11" height="8" fill="none" stroke="var(--ink)"/>
          <path d="M0.5 0.5 6 5l5.5-4.5" fill="none" stroke="var(--ink)"/>
        </svg>
        info@solvanaportugal.pt
      </li>
      <li>
        <svg width="12" height="12" viewBox="0 0 12 12" aria-hidden="true">
          <circle cx="6" cy="6" r="5.5" fill="none" stroke="var(--ink)"/>
          <ellipse cx="6" cy="6" rx="2.4" ry="5.5" fill="none" stroke="var(--ink)"/>
          <path d="M0.5 6h11" stroke="var(--ink)"/>
        </svg>
        www.solvanaportugal.pt
      </li>
    </ul>
  </section>

  <section class="card card-back" aria-label="Business card back">
    <div class="back-brand">
      <span class="brand-dot"></span>
      <span class="brand-name">Solvana Portugal</span>
    </div>
    <p class="web">www.solvanaportugal.pt</p>
  </section>
</main>
</body>
</html>
```